Kinesiology undergraduate program needs an infographic

We would like an infographic to creatively and succinctly inform students, faculty, staff, and others about our undergraduate values and competencies (perhaps also integrating our mission and vision). We would like to see a design that incorporates the definition of Kinesiology (the study of human movement) and the colors of our Westbrook State University at Larkfield.

```html
<!DOCTYPE html>
<html lang="en">
<head>
<meta charset="UTF-8">
<title>Our Values – WSUL Kinesiology</title>
<link rel="stylesheet" href="https://fonts.googleapis.com/css2?family=Montserrat:wght@700;800;900&family=Mulish:wght@400;500&display=swap">
<style>
  :root {
    --blue: #0180a7;
    --blue-dark: #006f8e;
    --blue-deep: #005a75;
    --tagline: #8fd3e8;
    --orange-a: #d15a00;
    --orange-b: #e56d05;
    --orange-strip: #e36a02;
    --teal-a: #169970;
    --teal-b: #158a70;
    --teal-strip: #0b7358;
    --green-a: #6a8d00;
    --green-b: #638700;
    --green-strip: #577800;
    --pink-a: #e0346b;
    --pink-b: #d70039;
    --pink-strip: #c21a4c;
    --white: #ffffff;
    --page: #f4f4f4;
  }
  * { margin: 0; padding: 0; box-sizing: border-box; }
  html, body { width: 1018px; height: 1200px; overflow: hidden; background: var(--page); }
  .poster {
    width: 1018px; height: 1200px;
    display: flex; flex-direction: column;
    font-family: "Mulish", sans-serif; color: var(--white);
  }
  .masthead {
    height: 169px; background: var(--blue);
    display: flex; flex-direction: column; align-items: center; justify-content: center;
  }
  .masthead h1 {
    font-family: "Montserrat", sans-serif; font-weight: 900;
    font-size: 66px; line-height: 1; letter-spacing: 1px;
  }
  .masthead p { font-size: 34px; margin-top: 12px; font-weight: 400; }
  .competent {
    height: 50px; background: var(--blue-dark);
    display: flex; align-items: center; justify-content: center;
    color: var(--tagline); font-size: 25px; letter-spacing: 9px;
  }
  .domain { height: 212px; display: flex; position: relative; }
  .domain-photo {
    width: 234px; height: 100%;
    display: flex; align-items: center; justify-content: center; text-align: center;
  }
  .domain-label {
    font-family: "Montserrat", sans-serif; font-weight: 800;
    font-size: 18px; line-height: 1.3; text-shadow: 0 1px 3px rgba(0,0,0,.35);
  }
  .domain-strip { width: 28px; height: 100%; }
  .arrow-badge {
    position: absolute; left: 234px; top: 50%; transform: translateY(-50%);
    width: 56px; height: 56px; border-radius: 50%; background: var(--white);
    display: flex; align-items: center; justify-content: center;
  }
  .competencies {
    flex: 1; list-style: none; padding-left: 112px;
    display: flex; flex-direction: column; justify-content: center;
  }
  .competencies li { display: flex; align-items: center; font-size: 28px; line-height: 1.5; }
  .competencies.roomy li { line-height: 2.05; }
  .competencies.tight li { font-size: 27px; line-height: 1.33; }
  .tick { width: 32px; height: 32px; margin-right: 12px; flex: none; }
  .tight .tick { width: 26px; height: 26px; margin-right: 16px; margin-left: 6px; }

  .science .domain-photo { background: radial-gradient(circle at 55% 45%, #e07a2a, #a24a08 75%); }
  .science .domain-strip { background: var(--orange-strip); }
  .science .competencies { background: linear-gradient(90deg, var(--orange-a), var(--orange-b)); }
  .thinking .domain-photo { background: linear-gradient(180deg, #5d9a8e, #5c978c); }
  .thinking .domain-strip { background: var(--teal-strip); }
  .thinking .competencies { background: linear-gradient(90deg, var(--teal-a), var(--teal-b)); }
  .relations .domain-photo { background: linear-gradient(180deg, #8f9a56, #4e5a2a 80%); }
  .relations .domain-strip { background: var(--green-strip); }
  .relations .competencies { background: linear-gradient(90deg, var(--green-a), var(--green-b)); }
  .growth .domain-photo { background: linear-gradient(160deg, #c85877, #8c1a3a 85%); }
  .growth .domain-strip { background: var(--pink-strip); }
  .growth .competencies { background: linear-gradient(90deg, var(--pink-a), var(--pink-b)); }

  .statements {
    height: 133px; background: var(--blue); display: flex;
    border-top: 8px solid var(--blue-deep); border-bottom: 8px solid var(--blue-deep);
  }
  .statement-head {
    background: var(--blue-dark); display: flex; flex-direction: column;
    align-items: center; justify-content: center; gap: 14px;
    font-family: "Montserrat", sans-serif; font-weight: 800; font-size: 16px; letter-spacing: .5px;
  }
  .mission-head { width: 193px; }
  .vision-head { width: 178px; }
  .statement-text {
    display: flex; align-items: center; font-size: 15.5px; line-height: 1.38; padding: 0 10px;
  }
  .mission-text { width: 330px; }
  .vision-text { flex: 1; padding-left: 12px; }
</style>
</head>
<body>
<main class="poster">
  <header class="masthead">
    <h1>OUR VALUES</h1>
    <p>Student Success • Science • Service</p>
  </header>
  <div class="competent">OUR GRADUATES WILL BE COMPETENT IN...</div>

  <section class="domain science">
    <div class="domain-photo" role="img" aria-label="Glowing anatomical figure of a sprinting runner"><span class="domain-label">THE SCIENCE OF<br>KINESIOLOGY</span></div>
    <div class="domain-strip"></div>
    <div class="arrow-badge"><svg width="34" height="34" viewBox="0 0 24 24"><path d="M4 12h15M13 5l7 7-7 7" fill="none" stroke="#e0601a" stroke-width="3.2" stroke-linecap="round" stroke-linejoin="round"/></svg></div>
    <ul class="competencies roomy">
      <li><svg class="tick" viewBox="0 0 24 24"><path d="M21 11a9 9 0 1 1-4-7.5" fill="none" stroke="#fff" stroke-width="2.2" stroke-linecap="round"/><path d="M7 11.5l4 4L21 5" fill="none" stroke="#fff" stroke-width="2.4" stroke-linecap="round" stroke-linejoin="round"/></svg>Foundational Concepts of Kinesiology</li>
      <li><svg class="tick" viewBox="0 0 24 24"><path d="M21 11a9 9 0 1 1-4-7.5" fill="none" stroke="#fff" stroke-width="2.2" stroke-linecap="round"/><path d="M7 11.5l4 4L21 5" fill="none" stroke="#fff" stroke-width="2.4" stroke-linecap="round" stroke-linejoin="round"/></svg>Clinical Application</li>
      <li><svg class="tick" viewBox="0 0 24 24"><path d="M21 11a9 9 0 1 1-4-7.5" fill="none" stroke="#fff" stroke-width="2.2" stroke-linecap="round"/><path d="M7 11.5l4 4L21 5" fill="none" stroke="#fff" stroke-width="2.4" stroke-linecap="round" stroke-linejoin="round"/></svg>Scientific Communication</li>
    </ul>
  </section>

  <section class="domain thinking">
    <div class="domain-photo" role="img" aria-label="Student with glasses standing in a thoughtful pose"><span class="domain-label">THINKING AND<br>REASONING</span></div>
    <div class="domain-strip"></div>
    <div class="arrow-badge"><svg width="34" height="34" viewBox="0 0 24 24"><path d="M4 12h15M13 5l7 7-7 7" fill="none" stroke="#0b6e55" stroke-width="3.2" stroke-linecap="round" stroke-linejoin="round"/></svg></div>
    <ul class="competencies">
      <li><svg class="tick" viewBox="0 0 24 24"><path d="M21 11a9 9 0 1 1-4-7.5" fill="none" stroke="#fff" stroke-width="2.2" stroke-linecap="round"/><path d="M7 11.5l4 4L21 5" fill="none" stroke="#fff" stroke-width="2.4" stroke-linecap="round" stroke-linejoin="round"/></svg>Critical Thinking</li>
      <li><svg class="tick" viewBox="0 0 24 24"><path d="M21 11a9 9 0 1 1-4-7.5" fill="none" stroke="#fff" stroke-width="2.2" stroke-linecap="round"/><path d="M7 11.5l4 4L21 5" fill="none" stroke="#fff" stroke-width="2.4" stroke-linecap="round" stroke-linejoin="round"/></svg>Quantitative Reasoning</li>
      <li><svg class="tick" viewBox="0 0 24 24"><path d="M21 11a9 9 0 1 1-4-7.5" fill="none" stroke="#fff" stroke-width="2.2" stroke-linecap="round"/><path d="M7 11.5l4 4L21 5" fill="none" stroke="#fff" stroke-width="2.4" stroke-linecap="round" stroke-linejoin="round"/></svg>Scientific Inquiry</li>
      <li><svg class="tick" viewBox="0 0 24 24"><path d="M21 11a9 9 0 1 1-4-7.5" fill="none" stroke="#fff" stroke-width="2.2" stroke-linecap="round"/><path d="M7 11.5l4 4L21 5" fill="none" stroke="#fff" stroke-width="2.4" stroke-linecap="round" stroke-linejoin="round"/></svg>Concept Integration</li>
    </ul>
  </section>

  <section class="domain relations">
    <div class="domain-photo" role="img" aria-label="Group of colleagues giving a high five in an office"><span class="domain-label">RELATIONSHIPS<br>AND<br>COMMUNICATION</span></div>
    <div class="domain-strip"></div>
    <div class="arrow-badge"><svg width="34" height="34" viewBox="0 0 24 24"><path d="M4 12h15M13 5l7 7-7 7" fill="none" stroke="#3f5a12" stroke-width="3.2" stroke-linecap="round" stroke-linejoin="round"/></svg></div>
    <ul class="competencies">
      <li><svg class="tick" viewBox="0 0 24 24"><path d="M21 11a9 9 0 1 1-4-7.5" fill="none" stroke="#fff" stroke-width="2.2" stroke-linecap="round"/><path d="M7 11.5l4 4L21 5" fill="none" stroke="#fff" stroke-width="2.4" stroke-linecap="round" stroke-linejoin="round"/></svg>Cultural Competence</li>
      <li><svg class="tick" viewBox="0 0 24 24"><path d="M21 11a9 9 0 1 1-4-7.5" fill="none" stroke="#fff" stroke-width="2.2" stroke-linecap="round"/><path d="M7 11.5l4 4L21 5" fill="none" stroke="#fff" stroke-width="2.4" stroke-linecap="round" stroke-linejoin="round"/></svg>Professionalism</li>
      <li><svg class="tick" viewBox="0 0 24 24"><path d="M21 11a9 9 0 1 1-4-7.5" fill="none" stroke="#fff" stroke-width="2.2" stroke-linecap="round"/><path d="M7 11.5l4 4L21 5" fill="none" stroke="#fff" stroke-width="2.4" stroke-linecap="round" stroke-linejoin="round"/></svg>Leadership and Teamwork</li>
      <li><svg class="tick" viewBox="0 0 24 24"><path d="M21 11a9 9 0 1 1-4-7.5" fill="none" stroke="#fff" stroke-width="2.2" stroke-linecap="round"/><path d="M7 11.5l4 4L21 5" fill="none" stroke="#fff" stroke-width="2.4" stroke-linecap="round" stroke-linejoin="round"/></svg>Service Orientation/Citizenship</li>
    </ul>
  </section>

  <section class="domain growth">
    <div class="domain-photo" role="img" aria-label="Person writing plans on a whiteboard"><span class="domain-label">INTRAPERSONAL<br>GROWTH</span></div>
    <div class="domain-strip"></div>
    <div class="arrow-badge"><svg width="34" height="34" viewBox="0 0 24 24"><path d="M4 12h15M13 5l7 7-7 7" fill="none" stroke="#9a0f33" stroke-width="3.2" stroke-linecap="round" stroke-linejoin="round"/></svg></div>
    <ul class="competencies tight">
      <li><svg class="tick" viewBox="0 0 24 24"><path d="M21 11a9 9 0 1 1-4-7.5" fill="none" stroke="#fff" stroke-width="2.2" stroke-linecap="round"/><path d="M7 11.5l4 4L21 5" fill="none" stroke="#fff" stroke-width="2.4" stroke-linecap="round" stroke-linejoin="round"/></svg>Cultural Humility/Sensitivity</li>
      <li><svg class="tick" viewBox="0 0 24 24"><path d="M21 11a9 9 0 1 1-4-7.5" fill="none" stroke="#fff" stroke-width="2.2" stroke-linecap="round"/><path d="M7 11.5l4 4L21 5" fill="none" stroke="#fff" stroke-width="2.4" stroke-linecap="round" stroke-linejoin="round"/></svg>Integrity</li>
      <li><svg class="tick" viewBox="0 0 24 24"><path d="M21 11a9 9 0 1 1-4-7.5" fill="none" stroke="#fff" stroke-width="2.2" stroke-linecap="round"/><path d="M7 11.5l4 4L21 5" fill="none" stroke="#fff" stroke-width="2.4" stroke-linecap="round" stroke-linejoin="round"/></svg>Self-Directed</li>
      <li><svg class="tick" viewBox="0 0 24 24"><path d="M21 11a9 9 0 1 1-4-7.5" fill="none" stroke="#fff" stroke-width="2.2" stroke-linecap="round"/><path d="M7 11.5l4 4L21 5" fill="none" stroke="#fff" stroke-width="2.4" stroke-linecap="round" stroke-linejoin="round"/></svg>Dependability</li>
      <li><svg class="tick" viewBox="0 0 24 24"><path d="M21 11a9 9 0 1 1-4-7.5" fill="none" stroke="#fff" stroke-width="2.2" stroke-linecap="round"/><path d="M7 11.5l4 4L21 5" fill="none" stroke="#fff" stroke-width="2.4" stroke-linecap="round" stroke-linejoin="round"/></svg>Mission Oriented</li>
    </ul>
  </section>

  <footer class="statements">
    <div class="statement-head mission-head">
      <svg width="42" height="42" viewBox="0 0 24 24"><path d="M22 2L2 10l8 3 3 8z" fill="#1aa6d0"/><path d="M22 2L10 13" stroke="#006f8e" stroke-width="1.4"/></svg>
      <span>OUR MISSION</span>
    </div>
    <p class="statement-text mission-text">To empower undergraduate students to pursue excellence through scientific discovery, clinical practice, and health promotion</p>
    <div class="statement-head vision-head">
      <svg width="52" height="34" viewBox="0 0 32 20"><path d="M1 10C5 3 10 1 16 1s11 2 15 9c-4 7-9 9-15 9S5 17 1 10z" fill="none" stroke="#1aa6d0" stroke-width="2"/><circle cx="16" cy="10" r="6" fill="#1aa6d0"/><circle cx="14" cy="8" r="1.8" fill="#006f8e"/></svg>
      <span>OUR VISION</span>
    </div>
    <p class="statement-text vision-text">WSUL Kinesiology graduates are leaders who excel in careers that enhance the quality of life of individuals and communities</p>
  </footer>
</main>
</body>
</html>
```